Flyer design for new conveyancing business

A flyer to email to real estate agents for referrals for conveyancing work.
Business name "Stonebridge Conveyancing"
Must give a very professional image. Preference is to use images of water etc.
must also contain the following details
Phone: 40912647
admin@stonebridgehomes.com.au
"For all your conveyancing needs from contract to completion"

Target Market(s)

people buying real estate

Industry/Entity Type

Real Estate

Font styles to use
Sans Serif

Colors
33b8a4
33a6d7
86cfc7
85cae6
0556a4

Requirements
Must have
• contact details
• clear text
Should not have
• be too busy

```html
<!DOCTYPE html>
<html lang="en">
<head>
<meta charset="utf-8">
<title>Stonebridge Conveyancing Flyer</title>
<link rel="stylesheet" href="https://fonts.googleapis.com/css2?family=Oswald:wght@500&family=Questrial&display=swap">
<style>
  :root {
    --water-light: #9ad8f2;
    --water-mid: #3fb0e2;
    --water-deep: #1f93d4;
    --wave-tone: rgba(255, 255, 255, 0.14);
    --ink: #161a1e;
    --white: #ffffff;
  }
  html, body { margin: 0; padding: 0; overflow: hidden; background: var(--water-deep); }
  .flyer {
    position: relative;
    width: 949px;
    height: 1200px;
    overflow: hidden;
    font-family: "Questrial", "Century Gothic", sans-serif;
    color: var(--ink);
  }
  .water-backdrop {
    position: absolute; inset: 0;
    background:
      radial-gradient(ellipse 120% 30% at 50% 4%, rgba(255,255,255,0.55), rgba(255,255,255,0) 70%),
      linear-gradient(180deg, var(--water-light) 0%, var(--water-mid) 22%, var(--water-mid) 60%, var(--water-deep) 100%);
  }
  .block { position: absolute; margin: 0; font-weight: 400; }
  .tagline {
    top: 150px; left: 0; width: 100%; text-align: center;
    font-family: "Oswald", "Arial Narrow", sans-serif;
    font-weight: 500; font-size: 64px; letter-spacing: -1.5px; line-height: 1;
  }
  .quote {
    top: 239px; left: 0; width: 100%; text-align: center;
    font-size: 36px; line-height: 44px;
  }
  .think-of {
    top: 373px; left: 0; width: 100%; text-align: center;
    font-size: 38px; line-height: 46px;
  }
  .business-name {
    top: 430px; left: 0; width: 100%; text-align: center;
    font-size: 68px; line-height: 82px; color: var(--white); letter-spacing: -0.5px;
    -webkit-text-stroke: 1.5px var(--ink);
    text-shadow: 3px 3px 0 var(--ink);
  }
  .wave-ornament {
    position: absolute;
    background: var(--wave-tone);
    border-radius: 40px;
  }
  .wave-ornament-top { left: 125px; top: 517px; width: 697px; height: 94px; }
  .wave-ornament-bottom { left: 312px; top: 1040px; width: 637px; height: 93px; border-radius: 40px 0 0 40px; }
  .intro-heading {
    top: 651px; left: 128px; font-size: 36px; line-height: 43px;
  }
  .intro-body {
    top: 702px; left: 174px;
    font-size: 24px; line-height: 34px;
  }
  .quote-prompt { top: 842px; left: 128px; font-size: 28px; line-height: 34px; }
  .phone {
    top: 890px; left: 226px;
    display: flex; align-items: center; gap: 15px;
    font-size: 88px; line-height: 1;
  }
  .phone-icon { width: 44px; height: 60px; }
  .email {
    top: 982px; left: 0; width: 100%; text-align: center;
    font-size: 36px; line-height: 44px;
  }
  .brand-sign {
    top: 1078px; left: 57px;
    font-size: 27px; line-height: 32px; color: var(--ink);
  }
</style>
</head>
<body>
  <main class="flyer">
    <div class="water-backdrop" role="img" aria-label="Photograph of clear rippling blue water filling the flyer"></div>

    <h1 class="block tagline">SERVICE • QUALITY • RESULTS</h1>
    <p class="block quote">“For all your conveyancing needs<br>from contract to completion”</p>
    <p class="block think-of">~ think of ~</p>
    <h2 class="block business-name">Stonebridge Conveyancing</h2>

    <div class="wave-ornament wave-ornament-top" role="img" aria-label="Decorative white wavy lines"></div>

    <h3 class="block intro-heading">We can handle your conveyancing.</h3>
    <p class="block intro-body">Our house legal team will handle your transaction smoothly,<br>making the complex process of buying or selling a breeze<br>for you. We offer a flat fee service.</p>

    <p class="block quote-prompt">Contact us for a quote.</p>
    <div class="block phone">
      <svg class="phone-icon" viewBox="0 0 44 64" aria-hidden="true">
        <path d="M14 4 C 6 10, 2 22, 4 34 C 6 46, 14 56, 24 62 L 30 52 C 22 46, 16 38, 15 30 C 14 22, 16 16, 22 12 Z" fill="var(--white)" stroke="var(--ink)" stroke-width="1.5"/>
      </svg>
      <span>40912647</span>
    </div>
    <p class="block email">admin@stonebridgehomes.com.au</p>

    <p class="block brand-sign">Stonebridge<br>Property Investment</p>

    <div class="wave-ornament wave-ornament-bottom" role="img" aria-label="Decorative white wavy lines"></div>
  </main>
</body>
</html>
```